Gewinnspielseite
Zielgruppe
Zielgruppe sind halt Gewinnspieler und Schnäppchenjäger
Aufgabenstellung
Es soll ein Design für eine Gewinnspielseite erstellt werden. Ich benötige eine Main-Seite die ruhig grafisch schön ist und dann eine Unterseite wo ich entsprechend Inhalte einspielen kann. Typische Gewinnspielseiten von uns unter www.kronmuehle.de wo die Unterseiten Contents dann auch gezeigt werden. Menüpunkte: Datenschutz, Teilnahmebedingungen, Impressum, Preis, Startseite

```html
<!DOCTYPE html>
<html lang="de">
<head>
<meta charset="utf-8">
<title>Gewinnspiel – LCD TV gewinnen</title>
<link rel="stylesheet" href="https://fonts.googleapis.com/css2?family=Fira+Sans:wght@500;700&family=Noto+Sans:wght@400;700&display=swap">
<style>
  :root {
    --outer: #a8c07c;
    --page: #ffffff;
    --blob: #c9da9c;
    --blob-dark: #b3c97c;
    --orange: #e8772e;
    --text: #3a3a3a;
    --label: #444444;
    --field-border: #9aa5b3;
    --footer: #8aab3a;
    --crowd: #e3ecd0;
    --note: #f0e79a;
    --tv: #2a2a2a;
  }
  * { box-sizing: border-box; margin: 0; padding: 0; }
  html, body { width: 1200px; height: 816px; overflow: hidden; }
  body { background: var(--outer); font-family: "Noto Sans", sans-serif; color: var(--text); position: relative; }
  .page { position: absolute; left: 102px; top: 0; width: 1000px; height: 816px; background: var(--page); overflow: hidden; }
  .abs { position: absolute; }

  .header-blob { left: -20px; top: -60px; width: 720px; height: 300px; }
  .headline { font-family: "Fira Sans", sans-serif; font-weight: 700; color: #fff; text-shadow: 2px 2px 3px rgba(0,0,0,.35); white-space: nowrap; }
  .headline-1 { left: 198px; top: 8px; font-size: 46px; }
  .headline-2 { left: 315px; top: 58px; font-size: 58px; }
  .headline-2 small { font-size: 36px; font-weight: 500; color: #fff; }
  .headline-3 { left: 222px; top: 122px; font-size: 82px; }

  .illu-woman { left: 40px; top: 0; width: 180px; height: 240px; border-radius: 40% 40% 10% 10%; background: linear-gradient(180deg, #f2b98a, #e99050 60%, #c7d3a0); opacity: .85; }
  .illu-tv { left: 633px; top: 142px; width: 332px; height: 262px; border-radius: 8px; background: linear-gradient(180deg, #444, var(--tv) 70%, #aaa); }
  .illu-note { left: 43px; top: 270px; width: 215px; height: 225px; background: var(--note); transform: rotate(-3deg); box-shadow: 4px 6px 8px rgba(0,0,0,.25); }
  .illu-marks { left: 0; top: 255px; width: 50px; height: 80px; background: linear-gradient(90deg, var(--orange), #f1a56e); opacity: .7; }
  .illu-stamp { left: 663px; top: 457px; width: 203px; height: 128px; background: linear-gradient(160deg, rgba(232,119,46,.55), rgba(232,119,46,.25)); transform: rotate(10deg); border-radius: 6px; }
  .illu-crowd { left: 0; top: 652px; width: 1000px; height: 138px; background: linear-gradient(180deg, rgba(227,236,208,.2), var(--crowd) 45%); }

  .intro { left: 298px; top: 290px; width: 330px; }
  .intro-title { color: var(--orange); font-size: 13.5px; font-weight: 700; margin-bottom: 12px; }
  .intro p { font-size: 10.5px; line-height: 14px; margin-bottom: 12px; }

  .entry { left: 298px; top: 474px; width: 460px; }
  .entry-title { font-size: 12px; font-weight: 700; letter-spacing: .3px; }
  .entry-lead { font-size: 10.5px; margin-top: 38px; }
  .form { margin-top: 38px; }
  .row { display: flex; align-items: center; height: 24.5px; font-size: 10.5px; color: var(--label); }
  .row label { width: 104px; }
  .field { height: 20px; border: 1px solid var(--field-border); background: #fff; }
  .field-wide { width: 237px; }
  .select { position: relative; height: 19px; border: 1px solid var(--field-border); background: #fff; font-size: 10px; padding-left: 3px; line-height: 17px; }
  .select::after { content: ""; position: absolute; right: 0; top: 0; width: 16px; height: 17px; background: #dfe5ee; border-left: 1px solid var(--field-border); }
  .select::before { content: ""; position: absolute; right: 4px; top: 7px; border: 4px solid transparent; border-top-color: #333; z-index: 1; }
  .dot { margin: 0 4px; }
  .submit { display: block; margin: 30px 0 0 352px; width: 91px; height: 15px; background: var(--orange); color: #fff; font-size: 8.5px; font-weight: 700; text-align: center; line-height: 15px; letter-spacing: .5px; border: none; }

  .footer { left: 0; top: 790px; width: 1000px; height: 26px; background: var(--footer); }
  .footer a { position: absolute; top: 7px; color: #fff; font-size: 10px; font-weight: 700; text-decoration: none; letter-spacing: .5px; }
</style>
</head>
<body>
<div class="page">
  <svg class="abs header-blob" viewBox="0 0 720 300" aria-hidden="true">
    <ellipse cx="360" cy="150" rx="360" ry="150" fill="var(--blob)"/>
    <ellipse cx="420" cy="215" rx="180" ry="60" fill="var(--blob-dark)" opacity=".6"/>
  </svg>
  <div class="abs illu-woman" role="img" aria-label="Illustration einer jubelnden Frau mit roten Haaren"></div>

  <div class="abs headline headline-1">Gewinnen Sie</div>
  <div class="abs headline headline-2">einen LCD TV <small>im Wert von</small></div>
  <div class="abs headline headline-3">2.000 € !</div>

  <div class="abs illu-tv" role="img" aria-label="Flachbildfernseher auf Standfuß"></div>
  <div class="abs illu-marks" role="img" aria-label="Orangefarbene handgezeichnete Striche"></div>
  <div class="abs illu-note" role="img" aria-label="Haftnotiz: 40 Zoll = 102 cm, 16:9 Format, HD Ready"></div>

  <div class="abs intro">
    <h1 class="intro-title">Herzlich Willkommen beim Gewinnspiel</h1>
    <p>Warum Sie bei diesem Gewinnspiel teilnehmen sollen?<br>Weil es Spaß macht, etwas zu gewinnen und weil der Gewinn sich wirklich sehen lassen kann:</p>
    <p>Es handelt sich um einen LCD TV mit einem Durchmesser von 102 cm, 16:9 Format und HD Ready im Wert von 2.000 Euro! Also, mitmachen und freuen!</p>
  </div>

  <div class="abs illu-stamp" role="img" aria-label="Stempelschrift: Jetzt gewinnen"></div>
  <div class="abs illu-crowd" role="img" aria-label="Silhouette einer jubelnden Menschenmenge"></div>

  <div class="abs entry">
    <h2 class="entry-title">GEWINNSPIELTEILNAHME</h2>
    <p class="entry-lead">Bitte tragen Sie sich nun für das kostenlose Gewinnspiel ein:</p>
    <div class="form">
      <div class="row"><label>Anrede:</label><div class="select" style="width:52px">—</div></div>
      <div class="row"><label>Vorname:</label><div class="field field-wide"></div></div>
      <div class="row"><label>Nachname:</label><div class="field field-wide"></div></div>
      <div class="row"><label>Geburtsdatum:</label>
        <div class="select" style="width:40px">—</div><span class="dot">.</span>
        <div class="select" style="width:98px">—</div><span class="dot">.</span>
        <div class="select" style="width:60px">—</div>
      </div>
      <div class="row"><label>E-Mail:</label><div class="field field-wide"></div></div>
      <button class="submit">ABSCHICKEN</button>
    </div>
  </div>

  <nav class="abs footer">
    <a href="#" style="left:198px">PREISDETAILS</a>
    <a href="#" style="left:341px">DATENSCHUTZ</a>
    <a href="#" style="left:488px">TEILNAHMEBEDINGUNGEN</a>
    <a href="#" style="left:704px">IMPRESSUM</a>
  </nav>
</div>
</body>
</html>
```